Renewable energy website needs a wordpress website

We are a Renewable Energy company specialising in Energy Management, LED Lights and Solar PV Systems based in Kuala Lumpur.
We need wordpress website designed to match our company identity.
We would like to stick with similar shades of blue & green as our logo and to keep it fresh and creative at the same time.

It Company

```html
<!DOCTYPE html>
<html lang="en">
<head>
<meta charset="utf-8">
<title>Verdant Current – Renewable Energy Systems</title>
<link href="https://fonts.googleapis.com/css2?family=Open+Sans:ital,wght@0,300;0,400;0,600;0,700;1,400&display=swap" rel="stylesheet">
<style>
:root{
  --cyan:#19d3ef;
  --green:#6cc04a;
  --ink:#222;
  --text:#555;
  --muted:#888;
  --grey-band:#efefef;
  --tile:#d4d4d4;
  --card:#f2f2f2;
  --footer:#262626;
  --white:#fff;
}
*{margin:0;padding:0;box-sizing:border-box}
html,body{width:1200px;height:2544px;overflow:hidden}
body{position:relative;background:var(--white);font-family:"Open Sans",Arial,sans-serif;color:var(--ink)}
.abs{position:absolute}

/* header */
.site-header{position:absolute;top:0;left:0;width:1200px;height:64px;background:var(--white);z-index:3}
.brand{position:absolute;left:227px;top:14px;display:flex;align-items:center;gap:10px}
.brand-dot{width:32px;height:32px;border-radius:50%;background:var(--cyan)}
.brand-name{font-size:15px;font-weight:700;color:var(--cyan);letter-spacing:1px;text-transform:uppercase;line-height:1}
.main-nav{position:absolute;right:210px;top:25px;display:flex;gap:17px;font-size:11px;font-weight:700;letter-spacing:.4px}
.main-nav a{color:var(--ink);text-decoration:none}
.search-btn{position:absolute;left:956px;top:22px;width:20px;height:20px;border:1px solid var(--cyan);border-radius:50%}

/* hero */
.hero{position:absolute;top:64px;left:0;width:1200px;height:414px;
  background:linear-gradient(180deg,#8d959d 0%,#a6adb3 40%,#7d8579 70%,#4d5836 100%);
  clip-path:polygon(0 0,100% 0,100% 84%,50% 100%,0 84%)}
.hero-brand{position:absolute;left:0;width:100%;top:96px;display:flex;justify-content:center;align-items:center;gap:12px}
.hero-brand .brand-dot{width:56px;height:56px}
.hero-brand .brand-name{font-size:26px;color:var(--white)}
.hero-title{position:absolute;top:210px;width:100%;text-align:center;color:var(--white);font-size:19px;font-weight:700;letter-spacing:3px}
.hero-sub{position:absolute;top:236px;width:100%;text-align:center;color:var(--white);font-size:19px;font-weight:300;letter-spacing:1.5px}
.hero-note{position:absolute;top:318px;width:100%;text-align:center;color:var(--white);font-size:10px;font-style:italic}
.hero-arrow{position:absolute;top:150px}
.hero-dots{position:absolute;top:366px;left:510px;width:180px;display:flex;align-items:center;gap:12px}
.hero-dots i{display:block;height:1px;flex:1;background:rgba(255,255,255,.5)}
.hero-dots b{width:5px;height:5px;border-radius:50%;background:var(--white)}
.hero-dots b.on{background:var(--cyan)}

/* section headings */
.section-title{position:absolute;left:0;width:1200px;text-align:center;font-size:15px;font-weight:700;letter-spacing:.4px}
.section-title::before{content:"";position:absolute;left:574px;top:-12px;width:52px;height:2px;background:var(--cyan)}

/* projects */
.projects-band{position:absolute;top:683px;left:0;width:1200px;height:330px;background:var(--grey-band);
  clip-path:polygon(0 0,100% 0,100% 90%,50% 100%,0 90%)}
.filters{position:absolute;top:559px;left:0;width:1200px;display:flex;justify-content:center;gap:12px}
.filters span{font-size:9px;font-weight:600;background:#e5e5e5;padding:3px 8px;color:#444}
.filters span.active{background:#3a3a3a;color:var(--white)}
.project-grid{position:absolute;top:600px;left:225px;display:grid;grid-template-columns:repeat(4,170px);grid-auto-rows:170px;column-gap:23px;row-gap:23px}
.project-tile{background:var(--tile);position:relative}
.project-hover{position:absolute;left:25px;top:25px;width:120px;height:120px;border-radius:50%;background:var(--cyan);color:var(--white);text-align:center;font-size:9px;font-weight:700;letter-spacing:.6px;line-height:2}
.project-hover svg{display:block;margin:28px auto 6px}

/* three columns */
.columns{position:absolute;left:225px;width:750px;display:grid;grid-template-columns:repeat(3,1fr);column-gap:40px}
.column h3{text-align:center;font-size:16px;font-weight:300;letter-spacing:.5px;color:#333;margin-bottom:10px}
.column p{text-align:center;font-size:8.5px;line-height:1.75;color:var(--text)}

/* LED cards */
.led-card{position:absolute;width:357px;height:128px;background:var(--card);z-index:2}
.led-card .tick{position:absolute;left:26px;top:26px}
.led-card h4{position:absolute;left:80px;top:26px;font-size:12px;font-weight:700;letter-spacing:1.3px}
.led-card p{position:absolute;left:80px;top:46px;width:255px;font-size:8.5px;line-height:1.7;color:var(--text)}

/* order band */
.order-band{position:absolute;top:1611px;left:0;width:1200px;height:206px;
  background:linear-gradient(180deg,#8a9298 0%,#9aa39e 35%,#5e6a40 75%,#3b4424 100%);
  clip-path:polygon(0 0,100% 0,100% 84%,50% 100%,0 84%)}
.order-title{position:absolute;top:1748px;width:1200px;text-align:center;color:var(--white);font-size:32px;font-weight:300;letter-spacing:.5px;z-index:2}
.btn{position:absolute;background:var(--cyan);color:var(--white);font-size:10px;letter-spacing:1px;text-align:center}
.order-btn{top:1806px;left:530px;width:140px;height:28px;line-height:28px}

/* contact */
.contact{position:absolute;top:2162px;left:0;width:1200px;height:248px;background:var(--grey-band)}
.contact-title{position:absolute;left:225px;top:38px;font-size:15px;font-weight:700}
.contact-title::before{content:"";position:absolute;left:0;top:-10px;width:52px;height:2px;background:var(--cyan)}
.field{position:absolute;background:var(--white);font-size:9px;color:#444;padding:6px 9px}
.team-title{position:absolute;left:785px;top:38px;font-size:11px;color:#444;letter-spacing:.5px}
.team-grid{position:absolute;left:787px;top:80px;display:grid;grid-template-columns:repeat(3,44px);gap:27px 27px}
.member{width:44px;height:44px;background:#cfcfcf;position:relative}
.member::before{content:"";position:absolute;left:15px;top:8px;width:14px;height:14px;border-radius:50%;background:var(--white)}
.member::after{content:"";position:absolute;left:9px;top:25px;width:26px;height:13px;border-radius:13px 13px 0 0;background:var(--white)}
.member.active::before,.member.active::after{display:none}
.member.active span{position:absolute;inset:0;border-radius:50%;background:var(--cyan)}

.cta-band{position:absolute;top:2410px;left:0;width:1200px;height:92px;background:var(--cyan);color:var(--white);text-align:center;line-height:92px;font-size:16px;letter-spacing:1.6px}
.cta-band strong{font-weight:700}
.cta-band span{font-weight:300}
.site-footer{position:absolute;top:2502px;left:0;width:1200px;height:42px;background:var(--footer);color:#9a9a9a;font-size:10px;letter-spacing:.5px}
.site-footer span{position:absolute;top:14px}
</style>
</head>
<body>

<header class="site-header">
  <div class="brand"><span class="brand-dot"></span><span class="brand-name">Verdant Current</span></div>
  <nav class="main-nav">
    <a href="#energy">ENERGY MANAGEMENT</a><a href="#led">LED LIGHTS</a><a href="#solar">SOLAR PV SYSTEMS</a><a href="#contact">CONTACTS</a><a href="#team">TEAM</a>
  </nav>
  <span class="search-btn"></span>
</header>

<section class="hero" role="img" aria-label="Photo of wind turbines on green hills under a cloudy sky">
  <div class="hero-brand"><span class="brand-dot"></span><span class="brand-name">Verdant Current</span></div>
  <h1 class="hero-title">RENEABLE ENERGY SYSTEMS</h1>
  <p class="hero-sub">BECAUSE WE CARE</p>
  <p class="hero-note">small lit am the sedist</p>
  <svg class="hero-arrow" style="left:240px" width="14" height="40" viewBox="0 0 14 40"><path d="M12 1 2 20l10 19" fill="none" stroke="#fff" stroke-width="1.5"/></svg>
  <svg class="hero-arrow" style="left:944px" width="14" height="40" viewBox="0 0 14 40"><path d="M2 1l10 19L2 39" fill="none" stroke="#fff" stroke-width="1.5"/></svg>
  <div class="hero-dots"><i></i><b class="on"></b><b></b><b></b><i></i></div>
</section>

<div class="projects-band"></div>
<h2 class="section-title" style="top:530px">OUR PROJECTS</h2>
<div class="filters"><span>ENERGY MANAGEMENT</span><span>LED LIGHTS</span><span>SOLAR PV SYSTEMS</span><span class="active">ALL</span></div>
<div class="project-grid">
  <div class="project-tile"></div><div class="project-tile"></div>
  <div class="project-tile"><div class="project-hover">
    <svg width="20" height="20" viewBox="0 0 20 20"><circle cx="8" cy="8" r="6" fill="none" stroke="#fff" stroke-width="2"/><path d="M12.5 12.5 18 18M8 5v6M5 8h6" stroke="#fff" stroke-width="2"/></svg>
    KUALA LUMPUR<br>SOLAR BATTERIES</div></div>
  <div class="project-tile"></div>
  <div class="project-tile"></div><div class="project-tile"></div><div class="project-tile"></div><div class="project-tile"></div>
</div>

<h2 class="section-title" id="energy" style="top:1066px">ENERGY MANAGEMENT</h2>
<div class="columns" style="top:1118px">
  <div class="column"><h3>TEAM</h3><p>Lorem ipsum dolor sit amet, consectetur adipiscing elit. Vivamus sit amet scelerisque orci. Donec molestie magna tincidunt lectus ornare, gravida molestie tortor imperdiet. In egestas accumsan orci, eget commodo odio ullamcorper id. Curabitur eget aliquam dui. Maecenas vehicula ullamcorper lectus, ac dictum est faucibus fermentum. Vestibulum sit amet lectus neque.</p></div>
  <div class="column"><h3>CLIENTS</h3><p>Vivamus iaculis urna id dictum tempor. Praesent gravida ante nec imperdiet dignissim. Donec lacinia eget mi eu convallis. Pellentesque nibh lacus, fringilla id neque sed, lacinia laoreet nulla. Proin varius vel felis eu aliquet. Maecenas erat libero, cursus at leo at, malesuada tempor mi, blandit elit accumsan.</p></div>
  <div class="column"><h3>WORK</h3><p>Donec suscipit dolor lectus, in eleifend nunc blandit et. Mauris quis lacus eu est fringilla condimentum vitae vel purus. Nunc cursus nisi nec adipiscing ornare. Donec eu ipsum sit amet libero blandit hendrerit eget in quam. Mauris luctus nunc et volutpat pretium. Nam hendrerit tortor in magna ultrices laoreet.</p></div>
</div>

<h2 class="section-title" id="led" style="top:1338px">LED LIGHTS</h2>

<div class="order-band" role="img" aria-label="Photo of a wind farm across green fields"></div>
<h2 class="order-title">Want to order?</h2>
<a class="btn order-btn">CONTACT US</a>

<article class="led-card" style="top:1391px;left:225px">
  <svg class="tick" width="36" height="36" viewBox="0 0 36 36"><circle cx="18" cy="18" r="16" fill="none" stroke="var(--cyan)" stroke-width="2"/><path d="M10 18l6 6 11-13" fill="none" stroke="var(--cyan)" stroke-width="3"/></svg>
  <h4>LED LIGHTS FOR HOME</h4>
  <p>Bacon ipsum dolor sit amet shank tri-tip pig, short loin pork belly boudin ground round flank sirloin bresaola fillet mignon sausage beef ribs kielbasa. Now freely, we have created a studio where we can not only work but also have fun and learn.</p>
</article>
<article class="led-card" style="top:1391px;left:615px">
  <svg class="tick" width="36" height="36" viewBox="0 0 36 36"><circle cx="18" cy="18" r="16" fill="none" stroke="var(--cyan)" stroke-width="2"/><path d="M10 18l6 6 11-13" fill="none" stroke="var(--cyan)" stroke-width="3"/></svg>
  <h4>LED FOR BUISINESS</h4>
  <p>Bacon ipsum dolor sit amet shank tri-tip pig, short loin pork belly boudin ground round flank sirloin bresaola fillet mignon sausage beef ribs kielbasa. Now freely, we have created a studio where we can not only work but also have fun and learn.</p>
</article>
<article class="led-card" style="top:1554px;left:225px">
  <svg class="tick" width="36" height="36" viewBox="0 0 36 36"><circle cx="18" cy="18" r="16" fill="none" stroke="var(--cyan)" stroke-width="2"/><path d="M10 18l6 6 11-13" fill="none" stroke="var(--cyan)" stroke-width="3"/></svg>
  <h4>WHOW IT WORKS</h4>
  <p>Bacon ipsum dolor sit amet shank tri-tip pig, short loin pork belly boudin ground round flank sirloin bresaola fillet mignon sausage beef ribs kielbasa. Now freely, we have created a studio where we can not only work but also have fun and learn.</p>
</article>
<article class="led-card" style="top:1554px;left:615px">
  <svg class="tick" width="36" height="36" viewBox="0 0 36 36"><circle cx="18" cy="18" r="16" fill="none" stroke="var(--cyan)" stroke-width="2"/><path d="M10 18l6 6 11-13" fill="none" stroke="var(--cyan)" stroke-width="3"/></svg>
  <h4>DEALERS</h4>
  <p>Bacon ipsum dolor sit amet shank tri-tip pig, short loin pork belly boudin ground round flank sirloin bresaola fillet mignon sausage beef ribs kielbasa. Now freely, we have created a studio where we can not only work but also have fun and learn.</p>
</article>

<h2 class="section-title" id="solar" style="top:1898px">SOLAR PV SYSTEMS</h2>
<div class="columns" style="top:1951px">
  <div class="column"><h3>TEAM</h3><p>Lorem ipsum dolor sit amet, consectetur adipiscing elit. Vivamus sit amet scelerisque orci. Donec molestie magna tincidunt lectus ornare, gravida molestie tortor imperdiet. In egestas accumsan orci, eget commodo odio ullamcorper id. Curabitur eget aliquam dui. Maecenas vehicula ullamcorper lectus, ac dictum est faucibus fermentum. Vestibulum sit amet lectus neque.</p></div>
  <div class="column"><h3>CLIENTS</h3><p>Vivamus iaculis urna id dictum tempor. Praesent gravida ante nec imperdiet dignissim. Donec lacinia eget mi eu convallis. Pellentesque nibh lacus, fringilla id neque sed, lacinia laoreet nulla. Proin varius vel felis eu aliquet. Maecenas erat libero, cursus at leo at, malesuada tempor mi, blandit elit accumsan.</p></div>
  <div class="column"><h3>WORK</h3><p>Donec suscipit dolor lectus, in eleifend nunc blandit et. Mauris quis lacus eu est fringilla condimentum vitae vel purus. Nunc cursus nisi nec adipiscing ornare. Donec eu ipsum sit amet libero blandit hendrerit eget in quam. Mauris luctus nunc et volutpat pretium. Nam hendrerit tortor in magna ultrices laoreet.</p></div>
</div>

<section class="contact" id="contact">
  <h2 class="contact-title">CONTACT US</h2>
  <div class="field" style="left:225px;top:78px;width:212px;height:26px">Name</div>
  <div class="field" style="left:225px;top:116px;width:212px;height:26px">Email</div>
  <div class="field" style="left:225px;top:154px;width:212px;height:26px">Phone</div>
  <div class="field" style="left:471px;top:78px;width:270px;height:102px">Comment</div>
  <a class="btn" style="left:625px;top:188px;width:116px;height:26px;line-height:26px">SEND LETTER</a>
  <h3 class="team-title" id="team">OUR TEAM</h3>
  <div class="team-grid">
    <div class="member"></div><div class="member active"><span></span></div><div class="member"></div>
    <div class="member"></div><div class="member"></div><div class="member"></div>
  </div>
</section>

<div class="cta-band"><strong>USE RENEABLE ENERGY SYSTEMS,</strong> <span>HELP THE PLANET</span></div>

<footer class="site-footer">
  <span style="left:225px">MEADOW LANE, 14/6</span>
  <span style="left:535px">HELLO@VERDANTCURRENT.COM</span>
  <span style="left:838px">(30100) 410 22718 40</span>
</footer>

</body>
</html>
```